Postcard for Construction Industry

www.quarrymarkestimates.com is our website.

We offer services to construction companies to read blueprints and give them a materials quantity list of how much work they need to do on a project. We service all types of companies such as painting, flooring, siding, drywall, Acoustical ceiling tile, framing, millwork, and much more.

I want a postcard designed that can be sent via email AND regular mail to introduce our company.

I've also attached another document with more detailed explanation, pricing, etc.

Important:
The postcard must appeal to the construction industry so they pick it up and read it.

Target Market(s)

Construction Industry

Industry/Entity Type

Construction

Font styles to use
Serif

Requirements
Must have
• Call to Action -
• Register on our site
• Get a FREE Quote
• Trades Serviced should be referenced on front so the person reading it immediately knows 2 things. Free Construction Takeoffs. List of Trades.
Nice to have
• Construction Images
• It's so EASY!!!
• -You load your plans
• -We give you a quote
• -If you approve, we do the work!
• NO OBLIGATION TO PURCHASE
Should not have
• Pricing - other than FREE Quotes
• Should not have phone number Prominent. It can be small on the back. (I want them to register via website)

```html
<!DOCTYPE html>
<html lang="en">
<head>
<meta charset="utf-8">
<title>QuarryMark Estimates Postcard</title>
<link rel="stylesheet" href="https://fonts.googleapis.com/css2?family=Exo+2:wght@600;700;800&family=Quicksand:wght@500;600;700&display=swap">
<style>
  :root {
    --navy: #1b3270;
    --navy-deep: #17306b;
    --bright: #1a93de;
    --sky-top: #8eaec6;
    --sky-mid: #b7cdd9;
    --ink: #1f2a3a;
    --white: #ffffff;
    --panel: #213f7e;
    --line: #9a9a9a;
  }
  * { margin: 0; padding: 0; box-sizing: border-box; }
  html, body { width: 802px; height: 1200px; overflow: hidden; background: #000; }
  body { position: relative; font-family: "Quicksand", sans-serif; }

  .card { position: absolute; left: 34px; width: 735px; overflow: hidden; }
  .front { top: 29px; height: 565px; background: linear-gradient(180deg, var(--sky-top) 0%, var(--sky-mid) 55%, #d8e2e4 70%); }
  .back { top: 606px; height: 564px; background: var(--white); }

  .brand { position: absolute; display: flex; align-items: center; gap: 8px;
    font-family: "Exo 2", sans-serif; font-weight: 700; color: var(--navy); font-size: 24px; letter-spacing: 0.5px; }
  .brand-mark { width: 12px; height: 12px; background: var(--navy); }
  .front .brand { left: 38px; top: 30px; }
  .back .brand { left: 72px; top: 30px; }

  .headline { position: absolute; left: 37px; top: 95px; font-family: "Exo 2", sans-serif; font-weight: 800;
    font-size: 23px; line-height: 25px; color: var(--navy); letter-spacing: 1.1px; }
  .easy { position: absolute; left: 40px; top: 154px; font-weight: 700; font-size: 21px; color: var(--ink); }
  .steps { position: absolute; left: 41px; top: 181px; font-size: 22px; line-height: 24.5px; color: var(--ink); font-weight: 500; list-style: none; letter-spacing: 0.3px; }
  .no-obligation { position: absolute; left: 40px; top: 287px; font-family: "Exo 2", sans-serif; font-weight: 600;
    font-size: 17px; letter-spacing: 1.1px; color: var(--bright); }

  .register { position: absolute; left: 454px; top: 33px; font-size: 14px; color: var(--white); }
  .site { position: absolute; left: 455px; top: 50px; font-weight: 700; font-size: 15.5px; color: var(--navy); letter-spacing: 0.3px; }
  .trades-tag { position: absolute; left: 451px; top: 98px; padding: 2px 6px; background: var(--navy);
    font-family: "Exo 2", sans-serif; font-weight: 800; font-size: 16.5px; letter-spacing: 1px; color: var(--white); }
  .trades-intro { position: absolute; left: 456px; top: 124px; font-size: 14px; line-height: 17.5px; color: var(--ink); white-space: nowrap; }
  .trades { position: absolute; top: 192px; list-style: none; font-size: 14.5px; line-height: 19px; color: var(--ink); }
  .trades li { position: relative; padding-left: 11px; margin-bottom: 5px; }
  .trades li::before { content: ""; position: absolute; left: 1px; top: 7px; width: 4px; height: 4px; border-radius: 50%; background: var(--bright); }
  .trades-a { left: 455px; }
  .trades-b { left: 579px; }

  .site-photo { position: absolute; left: 0; top: 315px; width: 735px; height: 226px;
    background:
      radial-gradient(ellipse 130px 90px at 150px 120px, rgba(70,120,170,0.85), rgba(70,120,170,0) 100%),
      radial-gradient(ellipse 95px 70px at 375px 135px, rgba(222,178,62,0.9), rgba(222,178,62,0) 100%),
      radial-gradient(ellipse 70px 50px at 560px 150px, rgba(40,90,160,0.75), rgba(40,90,160,0) 100%),
      radial-gradient(ellipse 200px 45px at 520px 180px, rgba(225,225,220,0.55), rgba(225,225,220,0) 100%),
      radial-gradient(ellipse 180px 60px at 660px 80px, rgba(60,70,80,0.45), rgba(60,70,80,0) 100%),
      linear-gradient(180deg, rgba(180,200,210,0) 0%, #a7a79d 35%, #8b7763 62%, #5a4636 100%); }
  .photo-tagline { position: absolute; left: 39px; top: 507px; font-weight: 600; font-size: 16.5px; color: var(--white); letter-spacing: 0.2px; text-shadow: 0 1px 3px rgba(0,0,0,0.5); }

  .values { position: absolute; left: 0; top: 541px; width: 735px; height: 24px; display: flex; }
  .values div { display: flex; align-items: center; justify-content: center; font-weight: 700; font-size: 15.5px; }
  .values .v-dark { background: var(--navy-deep); color: var(--bright); }
  .values .v-bright { background: var(--bright); color: var(--white); }

  .team-photo { position: absolute; left: 0; top: 75px; width: 366px; height: 489px;
    clip-path: polygon(0 0, 100% 32px, 100% 100%, 0 100%);
    background: linear-gradient(160deg, #2a4a8c 0%, var(--panel) 55%, #1b3468 100%); }
  .question { position: absolute; left: 83px; width: 187px; height: 67px; border: 1.5px solid var(--bright);
    display: flex; align-items: center; justify-content: center; text-align: center;
    font-family: "Exo 2", sans-serif; font-weight: 700; font-size: 16px; line-height: 18px; letter-spacing: 0.7px; color: var(--white); padding-top: 4px; white-space: nowrap; }
  .question.tall { padding-top: 8px; }
  .q-tab { position: absolute; left: 68px; top: -25px; width: 48px; height: 25px; }
  .pricing { position: absolute; left: 45px; top: 425px; font-size: 15px; color: var(--white); font-weight: 500; }
  .turnaround { position: absolute; left: 0; top: 453px; width: 366px; height: 21px; background: var(--bright);
    font-family: "Exo 2", sans-serif; font-weight: 800; font-size: 16px; letter-spacing: 0.8px; color: var(--white);
    display: flex; align-items: center; padding-left: 40px; }
  .contact { position: absolute; left: 0; top: 482px; width: 370px; text-align: center; color: var(--white);
    font-size: 14px; line-height: 16px; font-weight: 500; font-style: normal; }
  .contact strong { font-weight: 700; }

  .stamp { position: absolute; left: 601px; top: 46px; width: 94px; height: 101px; border: 1px solid var(--line); }
  .address-line { position: absolute; left: 418px; width: 282px; height: 1px; background: var(--line); }
</style>
</head>
<body>

<section class="card front">
  <div class="brand"><span class="brand-mark"></span>QuarryMark Estimates</div>

  <h1 class="headline">COMMERCIAL CONSTRUCTION<br>TAKEOFF SERVICES</h1>
  <p class="easy">It’s so EASY!!!</p>
  <ul class="steps">
    <li>You load your plans,</li>
    <li>We give you a quote</li>
    <li>If you approve,</li>
    <li>we do the work!</li>
  </ul>
  <p class="no-obligation">NO OBLIGATION TO PURCHASE</p>

  <p class="register">Register you project today</p>
  <p class="site">www.quarrymarkestimates.com</p>
  <h2 class="trades-tag">TRADES SERVICED</h2>
  <p class="trades-intro">Our experts will assist you with<br>commercial quantity takeoffs for<br>most construction trades including:</p>
  <ul class="trades trades-a">
    <li>Floor &amp;<br>Wallcoverings</li>
    <li>Painting</li>
    <li>Sheetrock</li>
  </ul>
  <ul class="trades trades-b">
    <li>Roofing</li>
    <li>Siding</li>
    <li>Foundations &amp;<br>Paving</li>
  </ul>

  <div class="site-photo" role="img" aria-label="Construction site with a tablet showing office towers, a yellow hard hat, rolled blueprints and a phone"></div>
  <p class="photo-tagline">Affordable, Professional, Commercial Blueprint Quantity Takeoffs</p>

  <div class="values">
    <div class="v-dark" style="width:234px">Experience</div>
    <div class="v-bright" style="width:268px">Reliable</div>
    <div class="v-dark" style="width:233px">Accurate</div>
  </div>
</section>

<section class="card back">
  <div class="brand"><span class="brand-mark"></span>QuarryMark Estimates</div>

  <div class="team-photo" role="img" aria-label="Overhead view of a team reviewing blueprints at a table, tinted blue"></div>

  <div class="question" style="top:126px">
    <svg class="q-tab" viewBox="0 0 48 25" aria-hidden="true">
      <path d="M0 25 V14 Q0 2 12 2 H36 Q48 2 48 14 V25" fill="none" stroke="#1a93de" stroke-width="1.5"/>
      <path d="M16 12 L22 18 L33 6" fill="none" stroke="#1a93de" stroke-width="4" stroke-linecap="round" stroke-linejoin="round"/>
    </svg>
    Can’t find the time<br>to bid new projects?
  </div>
  <div class="question tall" style="top:234px">
    <svg class="q-tab" viewBox="0 0 48 25" aria-hidden="true">
      <path d="M0 25 V14 Q0 2 12 2 H36 Q48 2 48 14 V25" fill="none" stroke="#1a93de" stroke-width="1.5"/>
      <path d="M16 12 L22 18 L33 6" fill="none" stroke="#1a93de" stroke-width="4" stroke-linecap="round" stroke-linejoin="round"/>
    </svg>
    Can’t find the budget<br>for a full-time<br>expert?
  </div>
  <div class="question tall" style="top:341px">
    <svg class="q-tab" viewBox="0 0 48 25" aria-hidden="true">
      <path d="M0 25 V14 Q0 2 12 2 H36 Q48 2 48 14 V25" fill="none" stroke="#1a93de" stroke-width="1.5"/>
      <path d="M16 12 L22 18 L33 6" fill="none" stroke="#1a93de" stroke-width="4" stroke-linecap="round" stroke-linejoin="round"/>
    </svg>
    Do you want to verify<br>the quantities from<br>your subs?
  </div>

  <p class="pricing">High-Volume Pricing Discounts Available</p>
  <p class="turnaround">Turnaround in as low as 24 hours!!</p>
  <address class="contact">
    Contact Us<br>
    <strong>Dale Hartwell</strong>, Owner<br>
    555-013-4872<br>
    Dale@QuarryMarkEstimates.com
  </address>

  <div class="stamp"></div>
  <div class="address-line" style="top:374px"></div>
  <div class="address-line" style="top:441px"></div>
  <div class="address-line" style="top:508px"></div>
</section>

</body>
</html>
```